Real Estate Newsletter

I would like a template created for a monthly newsletter; ideally, two pages long, including my photo, logo and contact info. I need it to look professional and be very easy for me to drop text into.

Target Market(s)

Past/current clients

Industry/Entity Type

Real Estate Agent

Font styles to use
Serif

Requirements
Must have
• My contact info/photo and logo
• (206) 555-0187
• mkettridge@lunvoro.com
• www.MarlaKettridge.com
Nice to have
• I need a template where I can easily drop contact. I need the template to look professional so I can print it and mail it to current and past clients.

```html
<!DOCTYPE html>
<html lang="en">
<head>
<meta charset="utf-8">
<title>Monthly Newsletter Templates – Marla Kettridge</title>
<link rel="stylesheet" href="https://fonts.googleapis.com/css2?family=Noto+Sans:ital,wght@0,400;0,700;1,400&family=Carlito:ital,wght@0,400;0,700;1,700&display=swap">
<style>
  :root {
    --paper: #ffffff;
    --sand: #f2ece1;
    --rule-blue: #7f9cc4;
    --ink: #1f1f1f;
    --slate: #5a5a5a;
    --panel-blue: #b1c5dc;
    --band-grey: #e2e1df;
    --navy: #2b4f8e;
    --logo-blue: #2d5fa6;
    --social-dark: #3b5a99;
    --social-light: #4fa6e0;
  }
  * { margin: 0; padding: 0; box-sizing: border-box; }
  html, body { width: 1200px; height: 3087px; overflow: hidden; background: var(--paper); }
  body { position: relative; color: var(--ink); font-family: "Noto Sans", Verdana, sans-serif; }
  .abs { position: absolute; white-space: nowrap; }
  .photo { position: absolute; }
  .size-tag { position: absolute; top: 10px; right: 12px; font: 700 19px "Noto Sans", sans-serif; color: #111; }

  /* Layout one */
  .one-header { left: 37px; top: 37px; width: 1163px; height: 295px; background: var(--sand); }
  .one-agent-photo { left: 87px; top: 106px; width: 240px; height: 159px; background: linear-gradient(160deg, #7f9fc8 0%, #b8a389 55%, #5d7a4a 100%); }
  .one-brand { left: 383px; top: 104px; font-size: 11px; font-weight: 700; color: var(--navy); }
  .one-contact { font-size: 19px; line-height: 25px; color: var(--ink); }
  .one-title { left: 387px; top: 162px; font-size: 64px; font-weight: 400; color: var(--slate); letter-spacing: 0.5px; }
  .one-date { left: 387px; top: 258px; font-size: 30px; }
  .rule { height: 3px; background: var(--rule-blue); }
  .one-heading { font-size: 34px; font-weight: 400; color: var(--slate); letter-spacing: 0.5px; }
  .one-body { font-size: 21px; }
  .one-hero { left: 626px; top: 389px; width: 495px; height: 535px; background: linear-gradient(120deg, #c8d79a 0%, #dde48f 40%, #e8c3a8 70%, #c97a4a 100%); }
  .one-tagline { left: 58px; top: 962px; width: 1071px; height: 58px; background: var(--sand); padding: 10px 29px; font-size: 28px; font-style: italic; color: var(--slate); white-space: nowrap; }
  .sold-card { width: 317px; height: 213px; top: 1115px; background: linear-gradient(180deg, #6f9fd6 0%, #d9d6c8 50%, #5f8a3e 100%); }
  .sold-address { top: 1347px; font-size: 21px; line-height: 28px; }
  .one-footer { left: 58px; top: 1428px; width: 1071px; height: 58px; background: var(--sand); }
  .one-footer-line { position: absolute; left: 29px; top: 17px; font-size: 19px; white-space: nowrap; }
  .one-footer-line span { margin-right: 24px; }
  .social-square { position: absolute; width: 42px; height: 42px; background: var(--social-dark); border-radius: 3px; }
  .social-dot { position: absolute; width: 42px; height: 42px; background: var(--social-light); border-radius: 50%; }

  /* Layout two */
  .two { font-family: "Carlito", Calibri, sans-serif; }
  .two-panel { left: 790px; top: 1554px; width: 410px; height: 1533px; background: var(--panel-blue); }
  .two-title-box { left: 0; top: 1610px; width: 531px; height: 116px; background: var(--band-grey); }
  .two-title { left: 77px; top: 1614px; font-size: 64px; font-weight: 700; }
  .two-sub { left: 77px; top: 1696px; font-size: 23px; }
  .two-brand { left: 540px; top: 1655px; font-size: 34px; font-weight: 700; color: var(--navy); }
  .two-heading { font-size: 31px; font-weight: 700; }
  .two-body { font-size: 19px; }
  .two-content-img { left: 468px; top: 1797px; width: 282px; height: 224px; background: linear-gradient(120deg, #d5df98 0%, #e2e291 45%, #e7c2a4 75%, #c4794b 100%); }
  .two-events-band { left: 0; top: 2197px; width: 758px; height: 317px; background: var(--band-grey); }
  .two-events-img { left: 73px; top: 2263px; width: 279px; height: 228px; background: linear-gradient(150deg, #8a8a8a 0%, #d9d9d9 45%, #f1f1f1 100%); }
  .two-pull { left: 75px; top: 2545px; font-size: 26px; font-weight: 700; font-style: italic; }
  .two-buyer-img { left: 452px; top: 2649px; width: 309px; height: 367px; background: linear-gradient(180deg, #d8cf9a 0%, #c4a98a 45%, #6d93c2 70%, #4f8a34 100%); }
  .two-agent-photo { left: 814px; top: 1633px; width: 313px; height: 209px; background: linear-gradient(160deg, #7ea3d1 0%, #c4b39c 55%, #6c7f5c 100%); }
  .two-logo-box { left: 817px; top: 1874px; width: 85px; height: 85px; background: var(--logo-blue); color: #fff; text-align: center; font-weight: 700; padding-top: 12px; }
  .two-logo-box .dims { font-size: 14px; line-height: 15px; }
  .two-logo-box .word { font-size: 22px; margin-top: 4px; letter-spacing: 1px; }
  .two-right { right: 77px; text-align: right; }
  .two-agent-name { top: 1880px; font-size: 26px; font-weight: 700; }
  .two-detail { font-size: 19px; line-height: 24px; }
  .two-social-text { font-size: 15px; line-height: 18px; right: 129px; text-align: right; }
  .two-divider { left: 814px; top: 2378px; width: 386px; height: 2px; background: #333; }
  .two-sold-card { left: 848px; width: 281px; height: 211px; background: linear-gradient(180deg, #6f9fd6 0%, #d9d6c8 50%, #5f8a3e 100%); }
</style>
</head>
<body>

<section class="layout-one">
  <div class="abs one-header"></div>
  <div class="photo one-agent-photo" role="img" aria-label="Agent portrait photo"></div>
  <div class="abs one-brand">MarlaKettridge</div>
  <div class="abs one-contact" style="left:487px; top:94px;">Marla Kettridge<br>(206) 555-0187</div>
  <div class="abs one-contact" style="left:668px; top:119px;">mkettridge@lunvoro.com</div>
  <div class="abs one-contact" style="left:928px; top:94px;">(Address)<br>City, State ZIP</div>
  <h1 class="abs one-title">NEWSLETTER TITLE</h1>
  <div class="abs one-date">Date | Sub Head</div>
  <div class="abs rule" style="left:0; top:337px; width:1129px;"></div>

  <h2 class="abs one-heading" style="left:87px; top:380px;">ARTICLE TITLE</h2>
  <p class="abs one-body" style="left:87px; top:445px;">Body Text</p>
  <div class="photo one-hero" role="img" aria-label="Photo of a hand passing house keys to another hand"><span class="size-tag">3.5"W x 3.8"H</span></div>

  <div class="abs one-tagline">Read this newsletter today and start saving tomorrow!</div>
  <div class="abs rule" style="left:0; top:1029px; width:1129px;"></div>

  <h2 class="abs one-heading" style="left:87px; top:1058px;">RECENTLY SOLD PROPERTIES</h2>
  <div class="photo sold-card" style="left:83px;" role="img" aria-label="Photo of a sold house"><span class="size-tag">2.25"W x 1.5"H</span></div>
  <div class="photo sold-card" style="left:452px;" role="img" aria-label="Photo of a sold house"><span class="size-tag">2.25"W x 1.5"H</span></div>
  <div class="photo sold-card" style="left:812px;" role="img" aria-label="Photo of a sold house"><span class="size-tag">2.25"W x 1.5"H</span></div>
  <p class="abs sold-address" style="left:87px;">(Address)<br>City, State ZIP</p>
  <p class="abs sold-address" style="left:456px;">(Address)<br>City, State ZIP</p>
  <p class="abs sold-address" style="left:816px;">(Address)<br>City, State ZIP</p>

  <footer class="abs one-footer">
    <p class="one-footer-line"><span>(Agent Name)</span><span>(Phone)</span><span>(Email Address)</span><span>(Address)</span><span>(City, State ZIP)</span></p>
    <div class="social-square" style="left:949px; top:8px;" aria-label="Social profile"></div>
    <div class="social-dot" style="left:1002px; top:8px;" aria-label="Social profile"></div>
  </footer>
  <div class="abs rule" style="left:0; top:1492px; width:1129px;"></div>
</section>

<section class="two">
  <div class="abs two-panel"></div>
  <div class="abs two-title-box"></div>
  <h1 class="abs two-title">Newsletter Title</h1>
  <div class="abs two-sub">Date | Subheader | Tagline</div>
  <div class="abs two-brand">MarlaKettridge</div>

  <h2 class="abs two-heading" style="left:77px; top:1755px;">Content Title</h2>
  <p class="abs two-body" style="left:77px; top:1808px;">Body Copy</p>
  <div class="photo two-content-img" role="img" aria-label="Photo of keys being handed over"><span class="size-tag">2"W x 1.6"H</span></div>
  <p class="abs two-body" style="left:77px; top:2033px;">Body Copy</p>

  <div class="abs two-events-band"></div>
  <h2 class="abs two-heading" style="left:77px; top:2210px;">Upcoming Events</h2>
  <div class="photo two-events-img" role="img" aria-label="Photo of a pen on a calendar page"><span class="size-tag">2"W x 1.6"H</span></div>
  <p class="abs two-body" style="left:383px; top:2274px;">- Upcoming Events</p>

  <p class="abs two-pull">Pay less on your new house than your current rent!</p>
  <h2 class="abs two-heading" style="left:77px; top:2602px;">Featured Buyer</h2>
  <p class="abs two-body" style="left:77px; top:2659px;">Body Copy</p>
  <div class="photo two-buyer-img" role="img" aria-label="Photo of a family in front of their new home"><span class="size-tag">2.2"W x 2.6"H</span></div>

  <div class="photo two-agent-photo" role="img" aria-label="Agent portrait photo"></div>
  <div class="abs two-logo-box"><div class="dims">0.6"W<br>x 0.6"H</div><div class="word">LOGO</div></div>
  <div class="abs two-right two-agent-name">(Agent Name)</div>
  <p class="abs two-right two-detail" style="top:1926px;">(Credentials)<br>DRE Lic. (000000)</p>
  <p class="abs two-right two-detail" style="top:2007px;">(Phone)<br>(Fax)<br>(Email Address)</p>
  <p class="abs two-right two-detail" style="top:2125px;">Address<br>City, State ZIP</p>

  <p class="abs two-social-text" style="top:2234px;">/yourname<br>or web address</p>
  <div class="social-square" style="left:1080px; top:2232px;" aria-label="Social profile"></div>
  <p class="abs two-social-text" style="top:2300px;">/yourname<br>or web address</p>
  <div class="social-dot" style="left:1080px; top:2298px;" aria-label="Social profile"></div>

  <div class="abs two-divider"></div>
  <h2 class="abs two-right two-heading" style="top:2396px;">Recently Sold</h2>
  <div class="photo two-sold-card" style="top:2450px;" role="img" aria-label="Photo of a sold house"><span class="size-tag">2"W x 1.5"H</span></div>
  <p class="abs two-right two-detail" style="top:2674px;">(Address)<br>(City, State ZIP)</p>
  <div class="photo two-sold-card" style="top:2740px;" role="img" aria-label="Photo of a sold house"><span class="size-tag">2"W x 1.5"H</span></div>
  <p class="abs two-right two-detail" style="top:2966px;">(Address)<br>(City, State ZIP)</p>
</section>

</body>
</html>
```